QUOTE Graphics for Summer Challenge

I would like to put these quotes over one of the pictures attached; For Instagram, use new size: 4:5 (1080 x 1350 pixels). One Quote per picture, and I want the quote to be bold or easy to read as well. I provided a few reference graphics that I really like as examples below.
All of the pictures are attached; you can pick any photo and add one quote to it; but no stock photography
All the quotes are in the attached WORD document

```html
<!DOCTYPE html>
<html lang="en">
<head>
<meta charset="utf-8">
<title>Summer Slimdown Quote Graphics</title>
<link rel="stylesheet" href="https://fonts.googleapis.com/css2?family=Bebas+Neue&family=Oswald:wght@300;400;500&family=Lato:wght@400;700;900&family=Dancing+Script:wght@600&display=swap">
<style>
:root{
  --board:#222023;
  --plum:#7a3a78;
  --plum-deep:#6a2f6c;
  --mauve:#9a5a92;
  --sky:#8fb6dc;
  --pool:#4fa3d4;
  --skin:#8a5a40;
  --pink:#f25a7a;
  --white:#ffffff;
}
*{margin:0;padding:0;box-sizing:border-box}
html,body{width:1200px;height:904px;overflow:hidden;background:var(--board)}
.board{position:relative;width:1200px;height:904px}
.tile{position:absolute;overflow:hidden;color:var(--white);
  background:linear-gradient(170deg,var(--plum) 0%,var(--mauve) 55%,var(--plum-deep) 100%)}
.tile.hero{left:35px;top:45px;width:462px;height:579px}
.tile.sq{width:209px;height:260px}
.photo{position:absolute;
  -webkit-mask-image:linear-gradient(90deg,transparent 0%,#000 35%);
  mask-image:linear-gradient(90deg,transparent 0%,#000 35%)}
.photo.sky-gown{background:linear-gradient(180deg,var(--sky) 0%,#a28aa8 40%,var(--skin) 60%,#7d6a50 100%)}
.photo.pool{background:linear-gradient(180deg,var(--sky) 0%,var(--skin) 45%,var(--pool) 100%)}
.photo.warm{background:linear-gradient(180deg,#b07a90 0%,var(--skin) 50%,#8c4a55 100%)}
.photo.rose{background:linear-gradient(180deg,#b0306a 0%,#c2506a 45%,#8c3a5a 100%)}
.photo.from-right{-webkit-mask-image:linear-gradient(270deg,transparent 0%,#000 40%);mask-image:linear-gradient(270deg,transparent 0%,#000 40%)}
.t{position:absolute;line-height:1}
.bebas{font-family:"Bebas Neue",sans-serif}
.oswald{font-family:"Oswald",sans-serif;font-weight:300}
.lato{font-family:"Lato",sans-serif}
.pink{color:var(--pink)}
.rule{position:absolute;height:1.5px;background:var(--pink)}
.handle{position:absolute;font-family:"Lato",sans-serif;font-style:italic;font-size:5.5px;bottom:11px}
.frame{position:absolute;border:1.5px solid var(--white)}
.tag{position:absolute;background:var(--pink);font-family:"Lato",sans-serif;font-size:7.5px;padding:3px 5px;clip-path:polygon(0 0,100% 0,93% 100%,0 100%)}
.vertical-title{white-space:nowrap;transform-origin:0 0;transform:rotate(-90deg) scaleX(.8)}
</style>
</head>
<body>
<main class="board">

  <section class="tile hero">
    <div class="photo sky-gown" role="img" aria-label="Photo of a smiling woman in a sheer olive cover-up gown on a poolside terrace" style="left:180px;top:0;width:282px;height:579px"></div>
    <p class="t lato" style="left:24px;top:20px;font-size:22px;font-weight:700;line-height:1.25">We’re getting a<br>tiny waist and<br>dropping pounds<br>together.</p>
    <h1 class="t bebas" style="left:20px;top:150px;font-size:104px;line-height:.86;font-weight:400">DON’T<br>MISS<br>THIS</h1>
    <p class="t lato" style="left:24px;top:445px;font-size:22px;line-height:1.25">COMMENT SUNKISSED<br>TO JOIN</p>
    <p class="t lato" style="left:24px;top:542px;font-size:11px;font-style:italic">@MayaBrooksFit</p>
  </section>

  <section class="tile sq" style="left:516px;top:45px">
    <div class="photo sky-gown" role="img" aria-label="Photo of a woman in an olive cover-up gown by a pool" style="left:90px;top:0;width:119px;height:260px"></div>
    <p class="t oswald" style="left:11px;top:8px;font-size:21px;line-height:1.03">YOU<br>DON’T NEED<br>MOTIVATION.</p>
    <div class="rule" style="left:11px;top:80px;width:33px;background:var(--white)"></div>
    <p class="t bebas" style="left:11px;top:92px;font-size:25px;line-height:.97">YOU NEED A<br>PROVEN PLAN<br>AND SOME<br>ACCOUNTABILITY</p>
    <p class="t lato" style="left:11px;top:202px;font-size:8px">Comment <b>SUNKISSED</b> to</p>
    <p class="tag" style="left:11px;top:213px">GET JOIN US ON JULY 7</p>
    <p class="handle" style="left:11px">@MayaBrooksFit</p>
  </section>

  <section class="tile sq" style="left:739px;top:45px">
    <div class="photo pool" role="img" aria-label="Photo of a woman in a leopard bikini sitting at an infinity pool edge" style="left:0;top:110px;width:209px;height:150px;-webkit-mask-image:linear-gradient(180deg,transparent 0%,#000 35%);mask-image:linear-gradient(180deg,transparent 0%,#000 35%)"></div>
    <p class="t bebas pink" style="left:15px;top:4px;font-size:74px;line-height:.85">SUMMER</p>
    <p class="t bebas pink" style="left:15px;top:64px;font-size:46px;line-height:.85">HERE</p>
    <p class="t lato" style="left:100px;top:67px;font-size:10px;line-height:1.22">BUT YOUR BODY<br>DOESN’T FEEL<br>READY?</p>
    <div class="rule" style="left:12px;top:116px;width:38px"></div>
    <p class="t oswald" style="left:11px;top:130px;font-size:17px;line-height:1">YOU’RE<br>NOT TOO<br>LATE.</p>
    <p class="t lato" style="right:11px;top:131px;font-size:10px;line-height:1.28;text-align:right">Comment<br>SUMMER<br>to join the<br><b style="color:var(--plum-deep)">Sunkissed<br>Summer<br>Slimdown</b></p>
    <p class="handle" style="right:10px">@MayaBrooksFit</p>
  </section>

  <section class="tile sq" style="left:964px;top:45px">
    <div class="photo warm" role="img" aria-label="Photo of a woman in a crochet dress outdoors" style="left:105px;top:0;width:104px;height:260px"></div>
    <p class="t bebas" style="left:10px;top:13px;font-size:14.5px;line-height:.98">YOUR BELLY BLOAT<br>AND STUBBORN<br>WEIGHT GAIN AREN’T<br>GOING ANYWHERE...</p>
    <div class="frame" style="left:9px;top:84px;width:102px;height:100px;border-right:none;border-bottom:none"></div>
    <div class="rule" style="left:9px;top:183px;width:102px;background:var(--white)"></div>
    <p class="t bebas" style="left:17px;top:89px;font-size:24px;line-height:.95"><span class="pink">UNLESS<br>YOU DO</span><br>SOMETHING<br>DIFFERENT.</p>
    <p class="t lato" style="left:10px;top:201px;font-size:7.5px">Comment SUNKISSED to</p>
    <p class="t lato" style="left:10px;top:210px;font-size:13px;font-weight:700">JOIN US!</p>
    <p class="handle" style="left:10px">@MayaBrooksFit</p>
  </section>

  <section class="tile sq" style="left:516px;top:322px">
    <div class="photo pool" role="img" aria-label="Photo of a woman in sunglasses and a black swimsuit in a pool" style="left:95px;top:0;width:114px;height:260px"></div>
    <p class="t lato" style="left:11px;top:12px;font-size:10px;font-weight:700;line-height:1.1">IF YOU FEEL<br>LIKE YOU’VE LET<br>YOURSELF GO LATELY,</p>
    <p class="t bebas" style="left:11px;top:57px;font-size:19px">THIS IS YOUR</p>
    <p class="t bebas" style="left:10px;top:75px;font-size:37px">JUMPSTART</p>
    <div class="rule" style="left:11px;top:115px;width:22px"></div>
    <p class="t lato" style="left:11px;top:130px;font-size:10px;line-height:1.22">COMMENT<br><b>SUMMER</b><br>TO JOIN THE</p>
    <p class="t bebas" style="left:11px;top:170px;font-size:19px;line-height:.92">SUNKISSED<br>SUMMER<br>SLIMDOWN</p>
    <p class="handle" style="left:11px">@MayaBrooksFit</p>
  </section>

  <section class="tile sq" style="left:739px;top:322px">
    <div class="photo rose" role="img" aria-label="Photo of a woman in a crochet top under pink light" style="left:60px;top:0;width:149px;height:260px"></div>
    <p class="t bebas" style="left:7px;top:8px;font-size:28px">NEED A</p>
    <p class="t bebas vertical-title" style="left:6px;top:252px;font-size:66px;line-height:.85">JUMPSTART?</p>
    <p class="t bebas" style="right:10px;top:156px;font-size:18.5px;line-height:.95;text-align:right">WE’RE DETOXING,<br>BURNING FAT, AND<br>GETTING SNATCHED.</p>
    <p class="t lato" style="right:10px;top:215px;font-size:7.5px;line-height:1.3;text-align:right">COMMENT SUNKISSED TO<br>JOIN US ON JULY 7TH</p>
    <p class="handle" style="right:10px">@MayaBrooksFit</p>
  </section>

  <section class="tile sq" style="left:964px;top:322px">
    <div class="photo pool" role="img" aria-label="Photo of a woman in sunglasses resting on an infinity pool edge" style="left:85px;top:0;width:124px;height:260px"></div>
    <p class="t bebas" style="left:10px;top:9px;font-size:23px;line-height:.93">CRAVINGS<br>BELLY FAT<br>AND WATER<br>WEIGHT?</p>
    <p class="t oswald" style="left:11px;top:116px;font-size:16px">SAY GOODBYE IN</p>
    <p class="t bebas pink" style="left:10px;top:132px;font-size:41px;line-height:.85">30 DAYS</p>
    <div class="rule" style="left:11px;top:170px;width:105px"></div>
    <p class="t lato" style="left:12px;top:183px;font-size:10px;line-height:1.25">Comment <b>SUMMER</b><br>to join the <b>Sunkissed</b><br><b>Summer Slimdown</b></p>
    <p class="handle" style="left:11px">@MayaBrooksFit</p>
  </section>

  <section class="tile sq" style="left:516px;top:596px">
    <div class="photo pool" role="img" aria-label="Photo of a woman in a leopard bikini seated by a pool" style="left:80px;top:40px;width:129px;height:220px"></div>
    <p class="t bebas" style="left:10px;top:9px;font-size:22px;line-height:.93">FEELING BLOATED,<br>SLUGGISH, AND TOO BIG?</p>
    <div class="frame" style="left:11px;top:63px;width:68px;height:92px"></div>
    <p class="t bebas pink" style="left:16px;top:66px;font-size:23px;line-height:.92">YOUR<br>DETOX<br>STARTS<br>NOW.</p>
    <p class="t lato" style="left:10px;top:170px;font-size:8.5px;line-height:1.15">Comment <b>SUMMER</b><br>to join the</p>
    <p class="t lato" style="left:10px;top:192px;font-size:12px;font-weight:900;line-height:.95">SUNKISSED<br>SUMMER<br>SLIMDOWN</p>
    <p class="handle" style="left:10px">@MayaBrooksFit</p>
  </section>

  <section class="tile sq" style="left:739px;top:596px">
    <div class="photo pool" role="img" aria-label="Photo of a woman in a black bikini wading in an infinity pool" style="left:80px;top:30px;width:129px;height:230px"></div>
    <p class="t bebas" style="left:10px;top:9px;font-size:20px;line-height:1">THE SCALE<br>KEEPS CLIMBING<br>AND NOTHING’S<br>WORKING?</p>
    <p class="t oswald" style="left:10px;top:101px;font-size:19px;line-height:1.05">THIS<br><span class="pink" style="font-weight:400">CHALLENGE</span><br>IS YOUR<br><span class="pink" style="font-weight:400">LIFELINE.</span></p>
    <p class="t lato" style="left:10px;top:196px;font-size:7.5px">Comment SUNKISSED to</p>
    <p class="tag" style="left:10px;top:205px;font-family:'Dancing Script',cursive;font-size:12px;padding:1px 10px 2px 6px">join now!</p>
    <p class="handle" style="left:10px">@MayaBrooksFit</p>
  </section>

  <section class="tile sq" style="left:964px;top:596px">
    <div class="photo sky-gown from-right" role="img" aria-label="Photo of a smiling woman in an olive cover-up gown by an infinity pool" style="left:0;top:0;width:130px;height:260px"></div>
    <p class="t bebas" style="right:9px;top:9px;font-size:30px;text-align:right">SUNKISSED</p>
    <p class="t bebas" style="right:8px;top:36px;font-size:52px;line-height:.85;text-align:right">SUMMER</p>
    <p class="t bebas" style="right:9px;top:83px;font-size:25px;text-align:right">SLIMDOWN</p>
    <p class="t lato" style="right:9px;top:120px;font-size:9.5px;line-height:1.25;text-align:right">plan is helping<br>women drop pounds<br>and feel sexy again.</p>
    <div class="frame" style="left:131px;top:172px;width:69px;height:49px"></div>
    <p class="t lato" style="right:15px;top:177px;font-size:8.5px;line-height:1.2;text-align:right">COMMENT<br>SUMMER TO<br><span style="font-size:13px">JOIN US</span></p>
    <p class="handle" style="right:11px">@MayaBrooksFit</p>
  </section>

</main>
</body>
</html>
```